Vodka label, brand name: LATE BIRCH

We are looking for a vodka label design, which will print on paper or plastic (not a bottle printing)

We are small distilling company: Ferncliff Distillery. Located in Toronto, Canada. Our business is small batches of handcrafted very smooth vodka production. 40% abv. Made from cane sugar and spring water.

Our audience pretty mach everyone who consume vodka/alcohol, we are not targeting any specific group.

Back label should have barcode, government warning and this text:

Our vodka is handmade in small batches to the highest standards befitting the true vodka perfectionist. We use silk filtering process for exceptional purity, clarity, and smoothness. It is distilled 6 times from the finest organic cane sugar using only the best Canadian spring water. Discover the smooth, clear taste for yourself.
Distilled and Bottled by
Ferncliff Distillery Inc.
Toronto, Canada

Government Warning: In accordance to the Surgeon General, women should not drink alcoholic beverages during pregnancy because of the risk of birth defects. Consumption of alcoholic beverages impairs your ability to drive a car or operate machinery and may cause health problems.

Size of the bottle as follows (see example in the attachment) :
Volume: 750ml
Total height: 330mm
Body diameter: 77mm
Closure: Bar Top
Silver synthetic cork

Target Market(s)

Colors

Designer to choose colors to be used in the design.

Requirements
Must have
• Incorporate the name: LATE BIRCH
• Incorporate: DISTILLED FROM ORGANIC CANE SUGAR
• Back bottle label should have barcode, government warning and this text:
• Our vodka is handmade in small batches to the highest standards befitting the true vodka perfectionist. We use silk filtering process for exceptional purity, clarity, and smoothness. It is distilled 6 times from the finest organic cane sugar using only the best Canadian spring water. Discover the smooth, clear taste for yourself.
• Distilled and Bottleb by
• Ferncliff Distillery Inc.
• Toronto, Canada
• Government Warning: In accordance to the Surgeon General, women should not drink alcoholic beverages during pregnancy because of the risk of birth defects. Consumption of alcoholic beverages impairs your ability to drive a car or operate machinery and may cause health problems.
Nice to have
• 1) To show in wording or design it was Handmade
• 2) To show in wording or design it was made with Natural Spring Water
• To show in wording or design it was made in small batches
• 3) To show in wording or design it was made local in Toronto, Canada
• "The Six" "The 6ix"- is the nick name of city of Toronto that's just for designer to consider and not mandatory to implement on design
Should not have
• We try to lower cost of printing , so design should be for digital printing without Gold, Silver or any other color which requires foil application on label and will increase cost of printing.
• No copy paste from internet images. Such designs will be ignored and reported to website admin. Authentic design work only.
• Please try not to use clock or any related to that images. Its nothing to do with clock, its too naive to show 6 pm on the watches in your design. Its could be time of the day (evening), after work, the six as nick name of Toronto. But not clock or watches .

```html
<!DOCTYPE html>
<html lang="en">
<head>
<meta charset="utf-8">
<title>LATE BIRCH Vodka – Front Label</title>
<link rel="stylesheet" href="https://fonts.googleapis.com/css2?family=Montserrat:wght@300;400;600;700&display=swap">
<style>
  :root {
    --page-bg: #eceeef;
    --label-slate: #4d6970;
    --label-slate-deep: #3f5a61;
    --wave-light: #e9edee;
    --wave-mid: #b9c6c9;
    --wave-dark: #7f9399;
    --ink-white: #ffffff;
    --ink-soft: #dbe4e6;
    --rule: rgba(255, 255, 255, 0.55);
  }
  * { margin: 0; padding: 0; box-sizing: border-box; }
  html, body {
    width: 849px;
    height: 1200px;
    overflow: hidden;
    background: var(--page-bg);
    font-family: "Montserrat", sans-serif;
  }
  .canvas {
    position: relative;
    width: 849px;
    height: 1200px;
  }
  .front-label {
    position: absolute;
    left: 124px;
    top: 170px;
    width: 600px;
    height: 860px;
    display: flex;
    background: linear-gradient(180deg, var(--label-slate) 0%, var(--label-slate-deep) 100%);
    box-shadow: 0 2px 10px rgba(0, 0, 0, 0.12);
  }
  .wave-panel {
    width: 200px;
    height: 100%;
    background: linear-gradient(100deg, var(--wave-light) 0%, var(--wave-mid) 55%, var(--wave-dark) 100%);
  }
  .label-body {
    position: relative;
    flex: 1;
    padding: 70px 40px 60px 56px;
    color: var(--ink-white);
    display: flex;
    flex-direction: column;
  }
  .handmade-tag {
    position: absolute;
    left: 22px;
    top: 70px;
    writing-mode: vertical-rl;
    transform: rotate(180deg);
    font-size: 17px;
    font-weight: 600;
    letter-spacing: 4px;
    color: var(--ink-white);
  }
  .brand-block {
    display: flex;
    align-items: center;
    gap: 18px;
    margin-top: 40px;
    padding-bottom: 46px;
    border-bottom: 2px solid var(--rule);
  }
  .brand-dot {
    width: 22px;
    height: 22px;
    border-radius: 50%;
    background: var(--ink-white);
    flex-shrink: 0;
  }
  .brand-name {
    font-size: 46px;
    font-weight: 300;
    letter-spacing: 5px;
    line-height: 1.1;
    color: var(--ink-white);
  }
  .product-type {
    margin-top: 70px;
    font-size: 46px;
    font-weight: 700;
    letter-spacing: 4px;
  }
  .product-claim {
    margin-top: 14px;
    font-size: 23px;
    font-weight: 600;
    letter-spacing: 2px;
    line-height: 1.35;
  }
  .product-note {
    margin-top: 26px;
    font-size: 14px;
    font-weight: 400;
    line-height: 1.5;
    color: var(--ink-soft);
  }
  .origin {
    margin-top: auto;
    font-size: 24px;
    font-weight: 600;
    letter-spacing: 1px;
  }
</style>
</head>
<body>
  <main class="canvas">
    <section class="front-label">
      <div class="wave-panel" role="img" aria-label="Decorative silver wave pattern in light grey tones"></div>
      <div class="label-body">
        <span class="handmade-tag">HANDMADE</span>
        <div class="brand-block">
          <span class="brand-dot"></span>
          <span class="brand-name">LATE BIRCH</span>
        </div>
        <h1 class="product-type">VODKA</h1>
        <p class="product-claim">DISTILLED FROM<br>ORGANIC CANE SUGAR</p>
        <p class="product-note">made with natural spring water,<br>small batch</p>
        <p class="origin">Toronto · Canada</p>
      </div>
    </section>
  </main>
</body>
</html>
```